Velmora Supply Chain and Logistic Consulting

Please review the attached Business Card. I want as close to this card with the colors, fonts, and quality of the card as possible. The attached compass should replace the deer head on both sides of the card and the text should say:

Backside
Compass JPEG
Velmora
A Supply Chain and Logistics Consulting Company

Frontside
Velmora
Ravi Ostrander - Port Alder Bay
President
____________________________________
(727) 555-0193
VelmoraSCL@Quillpost.com
_____________________________________

Bottom Front Side

Target Market(s)

Businesses

Contact Information for Business Card

Backside
Compass JPEG
Velmora

Frontside
Velmora
President
(727) 555-0193
VelmoraSCL@Quillpost.com

Bottom Front Side

Font styles to use
Serif
Script

Colors

Designer to choose colors to be used in the design.

Requirements
Must have
• See attached card for reference
Nice to have
Should not have

```html
<!DOCTYPE html>
<html lang="en">
<head>
<meta charset="utf-8">
<title>Velmora – Business Card</title>
<link rel="stylesheet" href="https://fonts.googleapis.com/css2?family=Cinzel:wght@400;500&family=Tinos:wght@400;700&display=swap">
<style>
  :root {
    --navy: #0b2a52;
    --navy-deep: #08234a;
    --paper: #ffffff;
    --rule: #c9ccd2;
    --ink: #1b1f29;
    --muted: #3a3f4a;
    --silver: #9ea3ab;
    --stage: #5b5d61;
  }
  * { margin: 0; padding: 0; box-sizing: border-box; }
  html, body { width: 1200px; height: 802px; overflow: hidden; }
  body { position: relative; background: var(--stage); font-family: "Tinos", "Times New Roman", serif; }

  .card { position: absolute; top: 274px; width: 443px; height: 264px; overflow: hidden; }
  .card-front { left: 136px; background: var(--paper); }
  .card-back { left: 624px; background: var(--navy); }

  .brand-mark {
    position: absolute; left: 64px; top: 44px; width: 96px; height: 96px;
    border: 2px solid var(--navy); border-radius: 50%;
  }
  .brand-name {
    position: absolute; left: 0; width: 224px; top: 180px; text-align: center;
    font-family: "Tinos", "Times New Roman", serif; font-weight: 400;
    font-size: 21px; color: var(--navy);
  }
  .divider { position: absolute; left: 215px; top: 69px; width: 1px; height: 126px; background: var(--rule); }

  .person { position: absolute; left: 235px; top: 66px; color: var(--navy); }
  .person-name, .person-city { font-weight: 700; font-size: 19px; line-height: 24px; }
  .person-title { font-size: 15px; line-height: 20px; color: var(--muted); margin-top: 1px; }

  .contact { position: absolute; left: 235px; top: 160px; font-size: 14.5px; line-height: 19px; color: var(--ink); }
  .contact-line { display: flex; align-items: center; gap: 4px; white-space: nowrap; }
  .contact-line svg { width: 14px; height: 12px; fill: var(--ink); flex: none; }

  .tagline-band {
    position: absolute; left: 0; bottom: 0; width: 100%; height: 37px; background: var(--navy);
    display: flex; align-items: center; justify-content: center;
  }
  .tagline {
    font-family: "Cinzel", "Times New Roman", serif; font-size: 13.5px;
    color: var(--paper); letter-spacing: 0.3px; white-space: nowrap;
  }

  .back-field {
    position: absolute; inset: 0;
    background: radial-gradient(circle at 68% 48%, #143663 0%, var(--navy) 60%, var(--navy-deep) 100%);
  }
  .back-mark {
    position: absolute; left: 281px; top: 105px; width: 48px; height: 48px;
    border-radius: 50%; background: var(--silver);
  }
  .back-tagline { position: absolute; left: 0; width: 100%; top: 235px; text-align: center; }
</style>
</head>
<body>

<section class="card card-front">
  <div class="brand-mark"></div>
  <div class="brand-name">Velmora</div>
  <div class="divider"></div>

  <div class="person">
    <div class="person-name">Ravi Ostrander</div>
    <div class="person-city">Port Alder Bay</div>
    <div class="person-title">President</div>
  </div>

  <div class="contact">
    <div class="contact-line">
      <svg viewBox="0 0 14 12" aria-hidden="true"><path d="M1 3.5C1 2 3 1 7 1s6 1 6 2.5V5h-3V3.8H4V5H1z M3 6h8l1.5 5h-11z"/></svg>
      <span>(727) 555-0193</span>
    </div>
    <div class="contact-line">
      <svg viewBox="0 0 14 12" aria-hidden="true"><path d="M1 2h12v8H1z M2 3v.4L7 7l5-3.6V3z" fill-rule="evenodd"/></svg>
      <span>VelmoraSCL@Quillpost.com</span>
    </div>
  </div>

  <div class="tagline-band"><span class="tagline">A Supply Chain and Logistics Consulting Company</span></div>
</section>

<section class="card card-back">
  <div class="back-field" role="img" aria-label="Repeating faint brand pattern on navy"></div>
  <div class="back-mark"></div>
  <div class="back-tagline"><span class="tagline">A Supply Chain and Logistics Consulting Company</span></div>
</section>

</body>
</html>
```